Diabetes control iOS/Android app design

I need a modern app design with light colors that are easy on the eyes, This app is for diabetes control. Focusing on Sweet/carb control and its daily intake .. I have uploaded some wireframe pages to design . Light colors are preferred for design. I donot need too much Hussle and data on main page.
Name/title: Glucaro- Diabetes reversal

Target Market(s)

Diabetes patients

Industry/Entity Type

health

Colors
0094D4
00A9DD
6FCCEA
C7EBF8
E9F6FB
00AB8E
00BBA5
67D7C9
C6EFE9
E9F9F6
59FF00
82FF00
B8FF75
E3FFCB
F4FFEA
FFC000
F8CF3A
FAE287
FDF2CF
FEFAEE

Requirements
Should not have
• complicated design. It should be simple , modern and easy o eye.

```html
<!DOCTYPE html>
<html lang="en">
<head>
<meta charset="utf-8">
<title>Glucaro – Diabetes Control App Design</title>
<link rel="stylesheet" href="https://fonts.googleapis.com/css2?family=Inter:wght@400;500;600;700;800&display=swap">
<style>
:root{
  --blue:#0094D4;
  --blue-2:#00A9DD;
  --sky:#6FCCEA;
  --pale:#C7EBF8;
  --mist:#E9F6FB;
  --teal:#00AB8E;
  --yellow:#FFC000;
  --yellow-soft:#FDF2CF;
  --orange:#F7931E;
  --red:#E8453C;
  --ink:#1D2733;
  --muted:#8A97A6;
  --line:#E3EAF0;
  --page:#F3F5F8;
  --card:#FFFFFF;
}
*{box-sizing:border-box;margin:0;padding:0}
html,body{width:1200px;height:2400px;overflow:hidden}
body{position:relative;background:var(--page);font-family:"Inter",sans-serif;color:var(--ink)}

.page-title{position:absolute;top:62px;left:0;width:1200px;text-align:center;font-size:30px;font-weight:800;letter-spacing:.5px}
.meta{position:absolute;top:130px;left:0;width:1200px;display:flex;justify-content:center;gap:70px}
.meta-item{text-align:center}
.meta-label{font-size:11px;font-weight:600;color:var(--muted);letter-spacing:1.5px}
.meta-value{margin-top:6px;font-size:16px;font-weight:700}
.tool-dot{display:inline-block;width:18px;height:18px;border-radius:50%;background:var(--ink);margin-top:6px}

.section-label{position:absolute;font-size:11px;font-weight:700;color:var(--muted);letter-spacing:1.2px;text-transform:uppercase}

.screen{position:absolute;width:230px;border-radius:22px;overflow:hidden;background:linear-gradient(180deg,#F7FBFE 0%,var(--mist) 100%);box-shadow:0 8px 24px rgba(20,60,90,.12);transform-origin:top left}
.hero .screen{box-shadow:0 12px 30px rgba(20,60,90,.18)}

.status{display:flex;justify-content:space-between;align-items:center;padding:9px 16px 0;font-size:9px;font-weight:700}
.appbar{display:flex;align-items:center;gap:8px;padding:10px 12px 8px}
.appbar .title{flex:1;font-size:12px;font-weight:700}
.back{width:22px;height:22px;border-radius:8px;background:var(--card);display:flex;align-items:center;justify-content:center;box-shadow:0 1px 3px rgba(0,0,0,.06)}
.avatar{width:22px;height:22px;border-radius:50%;background:linear-gradient(135deg,#F2C9A8,#C98F6B)}

.card{margin:0 10px 8px;background:var(--card);border-radius:12px;padding:9px 10px;box-shadow:0 1px 4px rgba(20,60,90,.06)}
.card-title{font-size:9px;font-weight:700;margin-bottom:6px}
.legend{display:flex;gap:8px;font-size:7px;color:var(--muted);margin-bottom:4px}
.legend span{display:flex;align-items:center;gap:3px}
.legend i{width:6px;height:6px;border-radius:50%;display:inline-block}

.gauge{display:block;margin:2px auto 4px}
.notice{margin:0 10px 8px;background:var(--card);border-radius:10px;padding:7px 10px;display:flex;align-items:center;gap:7px;font-size:8.5px;font-weight:600}
.notice .dot{width:14px;height:14px;border-radius:50%;background:var(--pale);display:flex;align-items:center;justify-content:center}
.notice .dot::after{content:"";width:6px;height:6px;border-radius:50%;background:var(--blue)}
.notice .chev{margin-left:auto;color:var(--muted)}

.tabbar{position:absolute;left:0;right:0;bottom:0;height:42px;background:var(--card);display:flex;justify-content:space-around;align-items:center;border-top:1px solid var(--line)}
.tab-active{width:30px;height:30px;border-radius:50%;background:var(--blue);display:flex;align-items:center;justify-content:center;box-shadow:0 4px 10px rgba(0,148,212,.35)}

.report-row{display:flex;align-items:center;gap:8px;padding:7px 0;border-bottom:1px solid var(--line);font-size:8.5px}
.report-row:last-child{border-bottom:none}
.report-row .ico{width:18px;height:18px;border-radius:6px;background:var(--mist);display:flex;align-items:center;justify-content:center}
.report-row .ico::after{content:"";width:6px;height:6px;border-radius:2px;background:var(--blue-2)}
.report-row .val{margin-left:auto;font-weight:700;color:var(--blue)}

.info{display:flex;gap:8px;align-items:flex-start}
.info-icon{flex:none;width:26px;height:26px;border-radius:8px;background:var(--blue);display:flex;align-items:center;justify-content:center}
.info p{font-size:8.5px;line-height:1.45;color:var(--ink);font-weight:500}
.field-label{margin:6px 12px 4px;font-size:8.5px;font-weight:600;color:var(--muted)}
.field{margin:0 10px 8px;background:var(--card);border:1px solid var(--line);border-radius:9px;padding:8px 10px;font-size:9px;display:flex;justify-content:space-between;align-items:center}
.actions{position:absolute;left:10px;right:10px;bottom:14px;display:flex;gap:8px}
.btn{flex:1;height:28px;border-radius:9px;font-size:9px;font-weight:700;display:flex;align-items:center;justify-content:center}
.btn-outline{background:var(--card);border:1px solid var(--pale);color:var(--blue)}
.btn-primary{background:var(--blue);color:#fff}

.steps{display:flex;gap:4px;margin:0 12px 10px}
.steps i{flex:1;height:4px;border-radius:2px;background:var(--pale)}
.steps i.on{background:var(--blue)}
.subhead{margin:4px 12px 8px;font-size:10px;font-weight:700}
.diet{margin:0 10px 7px;background:var(--card);border-radius:10px;padding:7px 9px;display:flex;align-items:center;gap:8px;font-size:9px;font-weight:600}
.diet .thumb{width:26px;height:26px;border-radius:7px;flex:none}
.diet small{display:block;font-size:7.5px;color:var(--muted);font-weight:500;margin-top:1px}
.radio{margin-left:auto;width:13px;height:13px;border-radius:50%;border:1.5px solid var(--pale)}
.radio.on{border:4px solid var(--blue)}

.ring{position:relative;width:88px;height:88px;margin:4px auto 6px}
.ring-text{position:absolute;inset:0;display:flex;flex-direction:column;align-items:center;justify-content:center}
.ring-text b{font-size:22px;font-weight:800;color:var(--blue);line-height:1.1}
.ring-text span{font-size:7.5px;color:var(--muted);font-weight:600}
.lead{margin:0 14px 8px;font-size:8px;line-height:1.45;color:var(--muted);text-align:center}
.tip{margin:0 10px 8px;background:var(--mist);border:1px solid var(--pale);border-radius:12px;padding:9px 10px}
.tip-head{display:flex;align-items:center;gap:6px;font-size:9px;font-weight:700;margin-bottom:4px}
.tip-head i{width:14px;height:14px;border-radius:50%;background:var(--yellow)}
.tip p{font-size:7.5px;line-height:1.5;color:var(--ink)}

.streak{text-align:center}
.streak-caption{font-size:9px;font-weight:600;color:var(--muted);margin-top:10px}
.streak-art{width:72px;height:72px;margin:14px auto 8px;border-radius:16px;background:linear-gradient(180deg,var(--yellow-soft) 0%,#FAE287 100%)}
.streak-num{font-size:34px;font-weight:800;line-height:1}
.streak-label{font-size:10px;font-weight:600;color:var(--muted);margin-top:3px}
.pill-btn{margin:16px auto 0;width:170px;height:30px;border-radius:10px;background:var(--blue);color:#fff;font-size:9px;font-weight:700;display:flex;align-items:center;justify-content:center;gap:6px}

.splash{display:flex;flex-direction:column;align-items:center;justify-content:center;background:linear-gradient(180deg,#FFFFFF 0%,var(--mist) 100%)}
.brand-mark{width:38px;height:38px;border-radius:10px;background:var(--blue)}
.brand-name{margin-top:12px;font-size:24px;font-weight:800;color:var(--blue)}
.brand-tag{margin-top:6px;font-size:8.5px;font-weight:500;color:var(--muted)}

.footer{position:absolute;top:2340px;left:0;width:1200px;text-align:center;font-size:24px;font-weight:800;color:#D3D9E0;letter-spacing:1px}
</style>
</head>
<body>

<svg width="0" height="0" style="position:absolute" aria-hidden="true">
  <defs>
    <linearGradient id="areaBlue" x1="0" y1="0" x2="0" y2="1">
      <stop offset="0" stop-color="#00A9DD" stop-opacity=".35"/>
      <stop offset="1" stop-color="#00A9DD" stop-opacity="0"/>
    </linearGradient>
    <symbol id="ico-back" viewBox="0 0 16 16"><path d="M10 3 5 8l5 5" fill="none" stroke="#1D2733" stroke-width="1.8" stroke-linecap="round" stroke-linejoin="round"/></symbol>
    <symbol id="ico-home" viewBox="0 0 16 16"><path d="M2.5 7.5 8 3l5.5 4.5V13h-3.5V9.5h-4V13H2.5z" fill="none" stroke="#8A97A6" stroke-width="1.4" stroke-linejoin="round"/></symbol>
    <symbol id="ico-chart" viewBox="0 0 16 16"><path d="M3 13V8M8 13V3M13 13V6" stroke="#8A97A6" stroke-width="1.8" stroke-linecap="round"/></symbol>
    <symbol id="ico-plus" viewBox="0 0 16 16"><path d="M8 3v10M3 8h10" stroke="#fff" stroke-width="2" stroke-linecap="round"/></symbol>
    <symbol id="ico-user" viewBox="0 0 16 16"><circle cx="8" cy="5.5" r="2.8" fill="none" stroke="#8A97A6" stroke-width="1.4"/><path d="M2.8 13.5c.8-2.6 2.8-3.8 5.2-3.8s4.4 1.2 5.2 3.8" fill="none" stroke="#8A97A6" stroke-width="1.4" stroke-linecap="round"/></symbol>
    <symbol id="ico-cal" viewBox="0 0 16 16"><rect x="2.5" y="3.5" width="11" height="10" rx="2" fill="none" stroke="currentColor" stroke-width="1.4"/><path d="M2.5 7h11M5.5 2v3M10.5 2v3" stroke="currentColor" stroke-width="1.4" stroke-linecap="round"/></symbol>
    <symbol id="ico-bell" viewBox="0 0 16 16"><path d="M4 11V7.5a4 4 0 0 1 8 0V11l1 1.5H3z" fill="#fff"/><circle cx="8" cy="14" r="1.3" fill="#fff"/></symbol>
    <symbol id="status-icons" viewBox="0 0 40 10"><rect x="0" y="6" width="2.5" height="4" rx=".6" fill="#1D2733"/><rect x="4" y="4" width="2.5" height="6" rx=".6" fill="#1D2733"/><rect x="8" y="2" width="2.5" height="8" rx=".6" fill="#1D2733"/><rect x="12" y="0" width="2.5" height="10" rx=".6" fill="#1D2733"/><rect x="20" y="1" width="17" height="8" rx="2" fill="none" stroke="#1D2733" stroke-width="1"/><rect x="21.8" y="2.8" width="12" height="4.4" rx="1" fill="#1D2733"/><rect x="38" y="3.5" width="1.5" height="3" rx=".6" fill="#1D2733"/></symbol>
    <symbol id="gauge" viewBox="0 0 200 112">
      <path d="M20 100 A80 80 0 0 1 60 30.7" fill="none" stroke="#FFC000" stroke-width="26"/>
      <path d="M60 30.7 A80 80 0 0 1 140 30.7" fill="none" stroke="#F7931E" stroke-width="26"/>
      <path d="M140 30.7 A80 80 0 0 1 180 100" fill="none" stroke="#E8453C" stroke-width="26"/>
      <circle cx="100" cy="100" r="40" fill="#fff"/>
      <circle cx="100" cy="100" r="34" fill="#00A9DD"/>
      <text x="100" y="84" text-anchor="middle" font-family="Inter, sans-serif" font-size="8" font-weight="600" fill="#fff">Today</text>
      <text x="100" y="108" text-anchor="middle" font-family="Inter, sans-serif" font-size="24" font-weight="800" fill="#fff">4</text>
    </symbol>
    <symbol id="line-chart" viewBox="0 0 200 70">
      <path d="M0 70H200M0 47H200M0 24H200" stroke="#E3EAF0" stroke-width=".8"/>
      <path d="M0 50 C20 30 30 55 50 40 S80 15 100 35 S140 55 160 25 S190 30 200 20 L200 70 L0 70Z" fill="url(#areaBlue)"/>
      <path d="M0 50 C20 30 30 55 50 40 S80 15 100 35 S140 55 160 25 S190 30 200 20" fill="none" stroke="#0094D4" stroke-width="2"/>
    </symbol>
    <symbol id="double-line" viewBox="0 0 200 90">
      <path d="M0 88H200M0 60H200M0 32H200M0 4H200" stroke="#E3EAF0" stroke-width=".8"/>
      <path d="M0 60 C25 40 35 70 60 50 S95 20 120 45 S165 70 200 30 L200 90 L0 90Z" fill="url(#areaBlue)"/>
      <path d="M0 60 C25 40 35 70 60 50 S95 20 120 45 S165 70 200 30" fill="none" stroke="#0094D4" stroke-width="2"/>
      <path d="M0 40 C30 55 50 30 80 42 S130 60 160 48 S190 40 200 45" fill="none" stroke="#FFC000" stroke-width="2"/>
    </symbol>
    <symbol id="bar-chart" viewBox="0 0 200 100">
      <path d="M0 98H200M0 66H200M0 34H200M0 2H200" stroke="#E3EAF0" stroke-width=".8"/>
      <rect x="4" y="50" width="9" height="48" rx="2" fill="#6FCCEA"/>
      <rect x="20" y="30" width="9" height="68" rx="2" fill="#0094D4"/>
      <rect x="36" y="58" width="9" height="40" rx="2" fill="#6FCCEA"/>
      <rect x="52" y="22" width="9" height="76" rx="2" fill="#0094D4"/>
      <rect x="68" y="44" width="9" height="54" rx="2" fill="#6FCCEA"/>
      <rect x="84" y="14" width="9" height="84" rx="2" fill="#0094D4"/>
      <rect x="100" y="52" width="9" height="46" rx="2" fill="#6FCCEA"/>
      <rect x="116" y="26" width="9" height="72" rx="2" fill="#0094D4"/>
      <rect x="132" y="60" width="9" height="38" rx="2" fill="#6FCCEA"/>
      <rect x="148" y="34" width="9" height="64" rx="2" fill="#0094D4"/>
      <rect x="164" y="48" width="9" height="50" rx="2" fill="#6FCCEA"/>
      <rect x="180" y="20" width="9" height="78" rx="2" fill="#0094D4"/>
    </symbol>
    <symbol id="ring" viewBox="0 0 88 88">
      <circle cx="44" cy="44" r="38" fill="#fff" stroke="#C7EBF8" stroke-width="7"/>
      <circle cx="44" cy="44" r="38" fill="none" stroke="#0094D4" stroke-width="7" stroke-linecap="round" stroke-dasharray="170 239" transform="rotate(-90 44 44)"/>
    </symbol>
  </defs>
</svg>

<h1 class="page-title">DIABETES CONTROL IOS/ANDROID APP DESIGN</h1>
<div class="meta">
  <div class="meta-item"><div class="meta-label">FONTS</div><div class="meta-value">INTER</div></div>
  <div class="meta-item"><div class="meta-label">TOOLS</div><span class="tool-dot"></span></div>
</div>

<section class="hero">
  <div class="screen" style="left:60px;top:320px;height:460px;transform:scale(.85)">
    <div class="status"><span>9:41</span><svg width="40" height="10"><use href="#status-icons"/></svg></div>
    <div class="appbar"><div class="back"><svg width="12" height="12"><use href="#ico-back"/></svg></div><div class="title">Streak</div><div class="avatar" role="img" aria-label="User profile photo"></div></div>
    <div class="streak">
      <div class="streak-caption">Days without extra sugar</div>
      <div class="streak-art" role="img" aria-label="Flame illustration for the daily streak"></div>
      <div class="streak-num">8</div>
      <div class="streak-label">Days Streak</div>
      <div class="pill-btn"><svg width="11" height="11" style="color:#fff"><use href="#ico-cal"/></svg>Day Wise Calendar</div>
    </div>
    <div class="tabbar"><svg width="16" height="16"><use href="#ico-home"/></svg><svg width="16" height="16"><use href="#ico-chart"/></svg><div class="tab-active"><svg width="14" height="14"><use href="#ico-plus"/></svg></div><svg width="16" height="16"><use href="#ico-user"/></svg></div>
  </div>

  <div class="screen" style="left:272px;top:300px;height:460px;transform:scale(.85)">
    <div class="status"><span>9:41</span><svg width="40" height="10"><use href="#status-icons"/></svg></div>
    <div class="appbar"><div class="back"><svg width="12" height="12"><use href="#ico-back"/></svg></div><div class="title">Profile</div><div class="avatar" role="img" aria-label="User profile photo"></div></div>
    <div class="ring"><svg width="88" height="88"><use href="#ring"/></svg><div class="ring-text"><b>200</b><span>Kcal left</span></div></div>
    <p class="lead">Hello Sam, your plan is going well. Keep your sugar low this week.</p>
    <div class="tip"><div class="tip-head"><i></i>What is Sugar?</div><p>Sugar is a sweet carb found in many foods. Too much raises blood glucose, so keep daily intake within your limit and choose whole foods.</p></div>
    <div class="tabbar"><svg width="16" height="16"><use href="#ico-home"/></svg><svg width="16" height="16"><use href="#ico-chart"/></svg><div class="tab-active"><svg width="14" height="14"><use href="#ico-plus"/></svg></div><svg width="16" height="16"><use href="#ico-user"/></svg></div>
  </div>

  <div class="screen" style="left:485px;top:270px;height:470px">
    <div class="status"><span>9:41</span><svg width="40" height="10"><use href="#status-icons"/></svg></div>
    <div class="appbar"><div class="back"><svg width="12" height="12"><use href="#ico-back"/></svg></div><div class="title">Sugar Count</div><div class="avatar" role="img" aria-label="User profile photo"></div></div>
    <svg class="gauge" width="200" height="112"><use href="#gauge"/></svg>
    <div class="notice"><span class="dot"></span>Enjoy your sugary treat<span class="chev">›</span></div>
    <div class="card"><div class="card-title">Daily Sugar Intake Graph</div><svg width="190" height="90" viewBox="0 0 200 70" preserveAspectRatio="none"><use href="#line-chart"/></svg></div>
    <div class="tabbar"><svg width="16" height="16"><use href="#ico-home"/></svg><svg width="16" height="16"><use href="#ico-chart"/></svg><div class="tab-active"><svg width="14" height="14"><use href="#ico-plus"/></svg></div><svg width="16" height="16"><use href="#ico-user"/></svg></div>
  </div>

  <div class="screen" style="left:734px;top:300px;height:460px;transform:scale(.85)">
    <div class="status"><span>9:41</span><svg width="40" height="10"><use href="#status-icons"/></svg></div>
    <div class="appbar"><div class="back"><svg width="12" height="12"><use href="#ico-back"/></svg></div><div class="title">Rebate Monitors</div><div class="avatar" role="img" aria-label="User profile photo"></div></div>
    <div class="card"><div class="card-title">Daily Sugar Graph</div><div class="legend"><span><i style="background:var(--blue)"></i>Intake</span><span><i style="background:var(--yellow)"></i>Limit</span></div><svg width="190" height="90"><use href="#double-line"/></svg></div>
    <div class="card"><div class="card-title">Daily Weight Intake</div><svg width="190" height="95"><use href="#bar-chart"/></svg></div>
    <div class="tabbar"><svg width="16" height="16"><use href="#ico-home"/></svg><div class="tab-active"><svg width="14" height="14"><use href="#ico-plus"/></svg></div><svg width="16" height="16"><use href="#ico-user"/></svg></div>
  </div>

  <div class="screen" style="left:945px;top:320px;height:460px;transform:scale(.85)">
    <div class="status"><span>9:41</span><svg width="40" height="10"><use href="#status-icons"/></svg></div>
    <div class="appbar"><div class="back"><svg width="12" height="12"><use href="#ico-back"/></svg></div><div class="title">Refuse Plan</div></div>
    <div class="card"><div class="info"><div class="info-icon"><svg width="13" height="13"><use href="#ico-bell"/></svg></div><p>We are able to bring you a customized diabetes control plan.</p></div></div>
    <div class="field-label">Select start date</div>
    <div class="field"><span>01 Mar 2024</span><svg width="11" height="11" style="color:var(--muted)"><use href="#ico-cal"/></svg></div>
    <div class="actions"><div class="btn btn-outline">Back</div><div class="btn btn-primary">Next</div></div>
  </div>
</section>

<div class="section-label" style="left:110px;top:832px">Sugar Count</div>
<div class="screen" style="left:110px;top:852px;height:352px">
  <div class="status"><span>9:41</span><svg width="40" height="10"><use href="#status-icons"/></svg></div>
  <div class="appbar"><div class="back"><svg width="12" height="12"><use href="#ico-back"/></svg></div><div class="title">Sugar Count</div><div class="avatar" role="img" aria-label="User profile photo"></div></div>
  <svg class="gauge" width="180" height="100" viewBox="0 0 200 112"><use href="#gauge"/></svg>
  <div class="notice"><span class="dot"></span>Enjoy your sugary treat<span class="chev">›</span></div>
  <div class="card"><div class="card-title">Daily Sugar Intake Graph</div><svg width="190" height="62" viewBox="0 0 200 70" preserveAspectRatio="none"><use href="#line-chart"/></svg></div>
  <div class="tabbar"><svg width="16" height="16"><use href="#ico-home"/></svg><svg width="16" height="16"><use href="#ico-chart"/></svg><div class="tab-active"><svg width="14" height="14"><use href="#ico-plus"/></svg></div><svg width="16" height="16"><use href="#ico-user"/></svg></div>
</div>

<div class="section-label" style="left:370px;top:832px">Rebate Monitors</div>
<div class="screen" style="left:370px;top:852px;height:820px">
  <div class="status"><span>9:41</span><svg width="40" height="10"><use href="#status-icons"/></svg></div>
  <div class="appbar"><div class="back"><svg width="12" height="12"><use href="#ico-back"/></svg></div><div class="title">Rebate Monitors</div><div class="avatar" role="img" aria-label="User profile photo"></div></div>
  <div class="card"><div class="card-title">Daily Sugar Graph</div><div class="legend"><span><i style="background:var(--blue)"></i>Sugar Intake</span><span><i style="background:var(--yellow)"></i>Sugar Limit</span></div><svg width="190" height="110" viewBox="0 0 200 90" preserveAspectRatio="none"><use href="#double-line"/></svg></div>
  <div class="card"><div class="card-title">Daily Weight Intake</div><svg width="190" height="120" viewBox="0 0 200 100" preserveAspectRatio="none"><use href="#bar-chart"/></svg></div>
  <div class="card">
    <div class="card-title">Daily Report</div>
    <div class="report-row"><span class="ico"></span>Breakfast sugar<span class="val">12 g</span></div>
    <div class="report-row"><span class="ico"></span>Lunch sugar<span class="val">18 g</span></div>
    <div class="report-row"><span class="ico"></span>Snack sugar<span class="val">6 g</span></div>
    <div class="report-row"><span class="ico"></span>Dinner sugar<span class="val">10 g</span></div>
  </div>
  <div class="card">
    <div class="card-title">Weekly Summary</div>
    <div class="report-row"><span class="ico"></span>Average sugar<span class="val">11 g</span></div>
    <div class="report-row"><span class="ico"></span>Water intake<span class="val">6 cups</span></div>
    <div class="report-row"><span class="ico"></span>Steps today<span class="val">4,210</span></div>
  </div>
  <div class="tabbar"><svg width="16" height="16"><use href="#ico-home"/></svg><svg width="16" height="16"><use href="#ico-chart"/></svg><div class="tab-active"><svg width="14" height="14"><use href="#ico-plus"/></svg></div><svg width="16" height="16"><use href="#ico-user"/></svg></div>
</div>

<div class="section-label" style="left:630px;top:832px">Refuse Plan</div>
<div class="screen" style="left:630px;top:852px;height:352px">
  <div class="status"><span>9:41</span><svg width="40" height="10"><use href="#status-icons"/></svg></div>
  <div class="appbar"><div class="back"><svg width="12" height="12"><use href="#ico-back"/></svg></div><div class="title">Refuse Plan</div></div>
  <div class="card"><div class="info"><div class="info-icon"><svg width="13" height="13"><use href="#ico-bell"/></svg></div><p>We are able to bring you a customized diabetes control plan.</p></div></div>
  <div class="field-label">Select start date</div>
  <div class="field"><span>01 Mar 2024</span><svg width="11" height="11" style="color:var(--muted)"><use href="#ico-cal"/></svg></div>
  <div class="actions"><div class="btn btn-outline">Back</div><div class="btn btn-primary">Next</div></div>
</div>

<div class="section-label" style="left:890px;top:832px">Load Device</div>
<div class="screen splash" style="left:890px;top:852px;height:360px">
  <div class="brand-mark"></div>
  <div class="brand-name">Glucaro</div>
  <div class="brand-tag">Glucaro- Diabetes reversal</div>
</div>

<div class="screen splash" style="left:890px;top:1310px;height:360px">
  <div class="brand-mark"></div>
  <div class="brand-name">Glucaro</div>
  <div class="brand-tag">Glucaro- Diabetes reversal</div>
</div>

<div class="section-label" style="left:110px;top:1696px">Refuse Plan - One</div>
<div class="screen" style="left:110px;top:1716px;height:380px">
  <div class="status"><span>9:41</span><svg width="40" height="10"><use href="#status-icons"/></svg></div>
  <div class="appbar"><div class="back"><svg width="12" height="12"><use href="#ico-back"/></svg></div><div class="title">Refuse Plan</div></div>
  <div class="steps"><i class="on"></i><i class="on"></i><i></i><i></i></div>
  <div class="subhead">Choose a suggested diet</div>
  <div class="diet"><span class="thumb" role="img" aria-label="Photo of an oat bowl" style="background:linear-gradient(135deg,#F8CF3A,#D9A441)"></span><span>Oat Bowl<small>180 kcal · 4 g sugar</small></span><span class="radio on"></span></div>
  <div class="diet"><span class="thumb" role="img" aria-label="Photo of a green salad" style="background:linear-gradient(135deg,#67D7C9,#00AB8E)"></span><span>Green Salad<small>120 kcal · 2 g sugar</small></span><span class="radio"></span></div>
  <div class="diet"><span class="thumb" role="img" aria-label="Photo of a fruit mix" style="background:linear-gradient(135deg,#F7931E,#E8453C)"></span><span>Fruit Mix<small>150 kcal · 9 g sugar</small></span><span class="radio"></span></div>
  <div class="actions"><div class="btn btn-outline">Back</div><div class="btn btn-primary">Next</div></div>
</div>

<div class="section-label" style="left:370px;top:1696px">Profile</div>
<div class="screen" style="left:370px;top:1716px;height:380px">
  <div class="status"><span>9:41</span><svg width="40" height="10"><use href="#status-icons"/></svg></div>
  <div class="appbar"><div class="back"><svg width="12" height="12"><use href="#ico-back"/></svg></div><div class="title">Profile</div><div class="avatar" role="img" aria-label="User profile photo"></div></div>
  <div class="ring"><svg width="88" height="88"><use href="#ring"/></svg><div class="ring-text"><b>200</b><span>Kcal left</span></div></div>
  <p class="lead">Hello Sam, your plan is going well. Keep your sugar low this week.</p>
  <div class="tip"><div class="tip-head"><i></i>What is Sugar?</div><p>Sugar is a sweet carb found in many foods. Too much raises blood glucose, so keep daily intake within your limit.</p></div>
  <div class="card" style="padding:7px 10px"><div class="card-title" style="margin-bottom:2px">1 KG Mission</div><svg width="190" height="30" viewBox="0 0 200 70" preserveAspectRatio="none"><use href="#line-chart"/></svg></div>
</div>

<div class="section-label" style="left:630px;top:1696px">Scale</div>
<div class="screen" style="left:630px;top:1716px;height:380px">
  <div class="status"><span>9:41</span><svg width="40" height="10"><use href="#status-icons"/></svg></div>
  <div class="appbar"><div class="back"><svg width="12" height="12"><use href="#ico-back"/></svg></div><div class="title">Streak</div><div class="avatar" role="img" aria-label="User profile photo"></div></div>
  <div class="streak">
    <div class="streak-caption">Days without extra sugar</div>
    <div class="streak-art" role="img" aria-label="Flame illustration for the daily streak"></div>
    <div class="streak-num">8</div>
    <div class="streak-label">Days Streak</div>
    <div class="pill-btn"><svg width="11" height="11" style="color:#fff"><use href="#ico-cal"/></svg>Day Wise Calendar</div>
  </div>
  <div class="tabbar"><svg width="16" height="16"><use href="#ico-home"/></svg><svg width="16" height="16"><use href="#ico-chart"/></svg><div class="tab-active"><svg width="14" height="14"><use href="#ico-plus"/></svg></div><svg width="16" height="16"><use href="#ico-user"/></svg></div>
</div>

<div class="screen splash" style="left:890px;top:1836px;height:360px">
  <div class="brand-mark"></div>
  <div class="brand-name">Glucaro</div>
  <div class="brand-tag">Glucaro- Diabetes reversal</div>
</div>

<div class="footer">THANK YOU FOR WATCHING MY WORKS</div>

</body>
</html>
```